Business card design needed

I have a leadership coaching and consultancy business which specialises in the education sector. I would like a clean, professional design). The design needs to speak to strength, support, new learning, connections & a growth mindest.

I am also looking for a unique LOGO. This is very important.

Target Market(s)

Educational Leaders & executives

Industry/Entity Type

Leadership

Contact Information for Business Card

Marisa Holbeck
Principal Coach & Consultant
Marisa Holbeck Coaching & Consulting
0471 362 815
marisa.holbeck@fernmail.example
I also would like my friendbook, chirper and workring accounts to appear

Logo styles of interest
Lettermark Logo
Requirements
Must have
• A 2 sided business card with contact details on the back
A logo

```html
<!DOCTYPE html>
<html lang="en">
<head>
<meta charset="utf-8">
<title>Marisa Holbeck Coaching &amp; Consulting – Business Card</title>
<link href="https://fonts.googleapis.com/css2?family=Open+Sans:wght@600;700&display=swap" rel="stylesheet">
<style>
  :root {
    --brand-orange: #f06124;
    --paper-white: #ffffff;
    --stage-dark: #262626;
    --stage-mid: #3a3a3a;
  }
  * { margin: 0; padding: 0; box-sizing: border-box; }
  html, body {
    width: 1200px; height: 1200px; overflow: hidden;
    background: radial-gradient(circle at 50% 45%, var(--stage-mid), var(--stage-dark) 75%);
    font-family: "Open Sans", Arial, sans-serif;
  }
  .card {
    position: absolute; left: 150px; width: 900px; height: 514px;
    overflow: hidden; box-shadow: 0 14px 30px rgba(0,0,0,.45);
  }
  .card--front { top: 60px; background: var(--brand-orange); }
  .card--back { top: 626px; background: var(--paper-white); }

  .brand-lockup { position: absolute; display: flex; align-items: center; gap: 22px; }
  .brand-lockup__dot { width: 90px; height: 90px; border-radius: 50%; flex: none; }
  .brand-lockup__name { font-weight: 700; line-height: 1.15; }

  .card--front .brand-lockup { left: 250px; top: 190px; }
  .card--front .brand-lockup__dot { background: var(--paper-white); }
  .card--front .brand-lockup__name { color: var(--paper-white); font-size: 34px; }

  .card--back .brand-lockup { left: 36px; top: 212px; gap: 16px; }
  .card--back .brand-lockup__dot { width: 70px; height: 70px; background: var(--brand-orange); }
  .card--back .brand-lockup__name { color: var(--brand-orange); font-size: 22px; }

  .divider { position: absolute; top: 0; bottom: 0; }
  .divider--rule { left: 372px; width: 14px; background: var(--brand-orange); }
  .details-panel {
    position: absolute; left: 408px; top: 0; right: 0; bottom: 0;
    background: var(--brand-orange); color: var(--paper-white);
    padding: 70px 40px 0 44px;
  }
  .details-panel__name { font-size: 40px; font-weight: 700; letter-spacing: 1px; }
  .details-panel__role { font-size: 23px; font-weight: 700; margin-top: 4px; }
  .details-panel__company { font-size: 17px; font-weight: 600; margin-top: 6px; }
  .contact-list { list-style: none; margin-top: 38px; }
  .contact-list__item {
    display: flex; align-items: center; gap: 12px;
    font-size: 19px; font-weight: 700; margin-bottom: 10px;
  }
  .contact-list__icon {
    width: 22px; height: 22px; flex: none;
    border: 2px solid var(--paper-white); display: flex;
    align-items: center; justify-content: center;
  }
  .contact-list__icon--plain { background: var(--paper-white); }
</style>
</head>
<body>

<section class="card card--front" aria-label="Card front">
  <div class="brand-lockup">
    <span class="brand-lockup__dot"></span>
    <span class="brand-lockup__name">Marisa Holbeck<br>Coaching &amp; Consulting</span>
  </div>
</section>

<section class="card card--back" aria-label="Card back">
  <div class="brand-lockup">
    <span class="brand-lockup__dot"></span>
    <span class="brand-lockup__name">Marisa Holbeck<br>Coaching &amp; Consulting</span>
  </div>
  <div class="divider divider--rule"></div>
  <div class="details-panel">
    <h1 class="details-panel__name">Marisa Holbeck</h1>
    <p class="details-panel__role">Principal Coach &amp; Consultant</p>
    <p class="details-panel__company">Marisa Holbeck Coaching &amp; Consulting</p>
    <ul class="contact-list">
      <li class="contact-list__item">
        <span class="contact-list__icon">
          <svg width="14" height="14" viewBox="0 0 24 24"><path fill="#fff" d="M6.6 10.8a15 15 0 0 0 6.6 6.6l2.2-2.2c.3-.3.7-.4 1-.2 1.1.4 2.3.6 3.6.6.6 0 1 .4 1 1V20c0 .6-.4 1-1 1A17 17 0 0 1 3 4c0-.6.4-1 1-1h3.5c.6 0 1 .4 1 1 0 1.3.2 2.5.6 3.6.1.3 0 .7-.2 1z"/></svg>
        </span>0471 362 815
      </li>
      <li class="contact-list__item">
        <span class="contact-list__icon">
          <svg width="14" height="12" viewBox="0 0 24 18"><rect x="1" y="1" width="22" height="16" fill="none" stroke="#fff" stroke-width="2.5"/><path d="M1 1l11 9 11-9" fill="none" stroke="#fff" stroke-width="2.5"/></svg>
        </span>marisa.holbeck@fernmail.example
      </li>
      <li class="contact-list__item"><span class="contact-list__icon contact-list__icon--plain"></span>your friendbook link here</li>
      <li class="contact-list__item"><span class="contact-list__icon contact-list__icon--plain"></span>your chirper link here</li>
      <li class="contact-list__item"><span class="contact-list__icon contact-list__icon--plain"></span>your workring link here</li>
    </ul>
  </div>
</section>

</body>
</html>
```